Need Bold, Hip Card for Concert Ticket Website Velvet Stubs!

Hi there! I am putting together a business/website that sells event tickets (mostly concerts, but also some sports and theater). Think PassDepot, but much smaller. The site is called Velvet Stubs. I have a new logo (attached, with black/red/white color scheme), and am looking for a modern/cool/original business card design. Note that I am thinking of having the card itself in the shape of a ticket (die cut), so you may want to keep that in mind when designing, but I'm not set on that. I'm also open to alternative card sizes, thicknesses, glossy, spot UV, etc. in order to stand out. I'm attaching a potential die cut template and a sample card using that template in case you want to work with that.
Target Market(s)
Music fans, people that like going to see live events
Industry/Entity Type
Entertainment
Contact Information for Business Card
Information that I'd like to have:
website address - www.velvetstubs-example.com
phone number: 1-833-5VELVETS (835-3887)
my name - Delia Hart
Look and feel
Each slider illustrates characteristics of the customer's brand and the style your logo design should communicate.

```html
<!DOCTYPE html>
<html lang="en">
<head>
<meta charset="utf-8">
<title>Velvet Stubs – Business Card</title>
<link rel="stylesheet" href="https://fonts.googleapis.com/css2?family=Montserrat:wght@400;600;800&display=swap">
<style>
  :root {
    --page: #e9e4dc;
    --red-light: #a32020;
    --red-dark: #7c0406;
    --black-light: #2a2a2a;
    --black: #070707;
    --white: #ffffff;
    --text-soft: #f2e6e6;
  }
  * { margin: 0; padding: 0; box-sizing: border-box; }
  html, body { width: 1200px; height: 1200px; overflow: hidden; }
  body {
    background: var(--page);
    font-family: "Montserrat", sans-serif;
    position: relative;
  }
  .card {
    position: absolute;
    left: 165px;
    width: 870px;
    height: 497px;
    border-radius: 22px;
    overflow: hidden;
    box-shadow: 0 8px 24px rgba(0,0,0,0.22);
  }
  .card-front {
    top: 70px;
    background: radial-gradient(circle at 60% 65%, var(--red-light) 0%, var(--red-dark) 70%);
    color: var(--white);
  }
  .card-back {
    top: 633px;
    background: radial-gradient(circle at 48% 42%, var(--black-light) 0%, var(--black) 60%);
    display: flex;
    align-items: center;
    justify-content: center;
  }
  .holder { position: absolute; left: 78px; top: 68px; }
  .holder-name { font-weight: 600; font-size: 27px; letter-spacing: 0.3px; }
  .holder-role { font-weight: 400; font-size: 21px; margin-top: 6px; color: var(--text-soft); }
  .contact-list {
    position: absolute;
    left: 78px;
    top: 268px;
    list-style: none;
  }
  .contact-item {
    display: flex;
    align-items: center;
    gap: 16px;
    font-size: 22px;
    font-weight: 400;
    margin-bottom: 22px;
  }
  .contact-icon { width: 20px; height: 20px; flex: none; }
  .brand {
    display: flex;
    align-items: center;
    gap: 22px;
  }
  .brand-mark { width: 46px; height: 46px; background: var(--white); }
  .brand-name {
    font-weight: 800;
    font-size: 74px;
    color: var(--white);
    text-transform: uppercase;
    letter-spacing: 1px;
  }
</style>
</head>
<body>
  <section class="card card-front" aria-label="Card front">
    <div class="holder">
      <p class="holder-name">Delia Hart</p>
      <p class="holder-role">Owner</p>
    </div>
    <ul class="contact-list">
      <li class="contact-item">
        <svg class="contact-icon" viewBox="0 0 20 20" fill="none" stroke="currentColor" stroke-width="1.5">
          <rect x="5" y="1.5" width="10" height="17" rx="2"/><line x1="8.5" y1="15.5" x2="11.5" y2="15.5"/>
        </svg>
        1-833-5VELVETS (835-3887)
      </li>
      <li class="contact-item">
        <svg class="contact-icon" viewBox="0 0 20 20" fill="none" stroke="currentColor" stroke-width="1.5">
          <rect x="1.5" y="4" width="17" height="12" rx="1"/><polyline points="1.5,4 10,11 18.5,4"/>
        </svg>
        info@velvetstubs-example.com
      </li>
      <li class="contact-item">
        <svg class="contact-icon" viewBox="0 0 20 20" fill="none" stroke="currentColor" stroke-width="1.5">
          <circle cx="10" cy="10" r="8.5"/><ellipse cx="10" cy="10" rx="3.8" ry="8.5"/><line x1="1.5" y1="10" x2="18.5" y2="10"/>
        </svg>
        velvetstubs-example.com
      </li>
    </ul>
  </section>

  <section class="card card-back" aria-label="Card back">
    <div class="brand">
      <span class="brand-mark" aria-hidden="true"></span>
      <span class="brand-name">Velvet Stubs</span>
    </div>
  </section>
</body>
</html>
```